Design wireframe of E-commerce website *

We are a European online shoe store located in Sweden. The project is to redesign the first page of our e-commerce website https://kelvaro.se/skor
We want to receive creative ideas of what our website could look like while keeping all the functions and flows. The new design should be simple, lean and modern.
Specifications:
We have several guidelines for what we are expecting
- Redesign the frontend of our website first page https://kelvaro.se/skor and the child page https://www.kelvaro.se/skor/dam
- You need to provide a complete clickable wireframe of the target pages.
- All existing components should be in the new design.
- The pages should include all sections: header, footer, product lists and widgets. The page structure of the site should look as the example: https://www.trimsel.co.uk/shoes
- The design must be responsive and Mobile First which can be read from all browsers and different devices.
- You need to have in mind that we really want it to be mobile first, meaning
the mobile view is the most important one
- The new design should reflect our brands essence and come along with the new brandprofiles (fonts, icons...). For example http://brandprofile.trimsel.com/, but keep the logo and colour of the existing Kelvaro theme.
- The design should be user friendly.
- The design should be simple enough that the pages can be downloaded fast.
- The new design should look fashionable and be able to generating attracting
traffic.
- The text on the child page https://www.kelvaro.se/skor/dam should be handled in a better way and make it easier for users to know which page they are looking at. You can see the example at https://www.trimsel.co.uk/shoes/women but we are open to your good ideas as well.
- We do not want shelves in the design. Trimsel has it, but Kelvaro
should not.
- We want to keep the existing responsive sizes for product list which means 2, 4 or 6 pairs of shoes per row.
Practical Information:
We are located in Sweden and have working hours between 9:00 -12:00 (CEST)
Monday - Friday. We have limited capacity to answer every question you have
but will try to get back to you in our working hours as much as we can then
hopefully this can help you get a better understanding of what we are
looking for.
Future Possibilities:We are going to redesign the whole site
of https://www.kelvaro.se/skor so the winner
will have the chance to do all the pages in the near future. We are
actively seeking designers for future collaborations on a long-term basis
and it is possible to create a partnership if your work is impressive
enough. *

```html
<!DOCTYPE html>
<html lang="en">
<head>
<meta charset="utf-8">
<title>Kelvaro – Shoes</title>
<link href="https://fonts.googleapis.com/css2?family=Open+Sans:wght@400;600;700;800&display=swap" rel="stylesheet">
<style>
:root{
  --stage:#8f8f8f;
  --white:#ffffff;
  --green:#5cb85c;
  --green-dark:#4a9d4a;
  --ink:#2b2b2b;
  --muted:#8a8a8a;
  --line:#e3e3e3;
  --blue:#3b7fd1;
  --red:#e03a3a;
  --footer:#222222;
  --footer-text:#bdbdbd;
  --tile-brown:#6d5646;
  --tile-grey:#8d8d8d;
}
*{box-sizing:border-box;margin:0;padding:0}
html,body{width:1200px;height:2880px;overflow:hidden}
body{background:var(--stage);font-family:"Open Sans",Arial,sans-serif;color:var(--ink);position:relative}
.view{position:absolute;background:var(--white);overflow:hidden;display:flex;flex-direction:column}
.view--desktop{left:32px;top:32px;width:736px;height:2736px}
.view--mobile{left:888px;top:120px;width:280px;height:2640px}

/* header */
.topbar{display:flex;align-items:center;justify-content:space-between;padding:0 24px;height:44px}
.logo{font-weight:800;font-size:22px;letter-spacing:.5px;color:var(--ink);display:flex;align-items:center;gap:6px}
.logo-mark{width:10px;height:10px;background:var(--green)}
.header-icons{display:flex;gap:10px}
.header-icons svg{width:14px;height:14px}
.navbar{display:flex;align-items:center;justify-content:space-between;height:30px;padding:0 24px;border-top:1px solid var(--line);border-bottom:1px solid var(--line)}
.search{width:260px;height:18px;border:1px solid var(--line);font-size:8px;color:var(--muted);padding:2px 6px;display:flex;justify-content:space-between;align-items:center}
.nav-links{display:flex;gap:20px;font-size:9px;font-weight:700}

/* hero */
.hero{display:flex;margin:12px 24px 0;height:272px}
.hero-panel{background:var(--green);width:42%;padding:28px 22px;color:var(--white)}
.hero-title{font-size:20px;font-weight:800;line-height:1.2;margin-bottom:18px}
.select{background:var(--white);height:20px;margin-bottom:8px;font-size:8px;color:var(--muted);display:flex;align-items:center;justify-content:space-between;padding:0 8px}
.hero-photo{flex:1;background:linear-gradient(135deg,#5a4636,#a58a70 50%,#3b2f27)}

/* category tiles */
.tiles{display:grid;gap:5px;margin:12px 24px 0}
.tiles--four{grid-template-columns:repeat(4,1fr)}
.tiles--two{grid-template-columns:repeat(2,1fr);margin:8px 10px 0}
.tile{position:relative;height:114px}
.tile-photo{position:absolute;inset:0}
.tile-label{position:absolute;left:0;right:0;bottom:0;height:18px;background:var(--green);color:var(--white);font-size:8px;font-weight:700;padding:0 8px;display:flex;align-items:center}
.tone-a{background:linear-gradient(160deg,#b9b2a8,#6d6359)}
.tone-b{background:linear-gradient(160deg,#c44b3b,#5b3a33)}
.tone-c{background:linear-gradient(160deg,#d9d3c8,#8c8378)}
.tone-d{background:linear-gradient(160deg,#4a4a4a,#9a9a9a)}
.tone-e{background:linear-gradient(160deg,#7e6450,#2f2722)}
.tone-f{background:linear-gradient(160deg,#9fb7c9,#4f6575)}

/* promo */
.promo{margin:8px 24px 0;height:150px;display:flex;align-items:center;background:linear-gradient(90deg,#efece6 45%,#b98c5e 75%,#6b4b30);padding:0 34px;justify-content:space-between}
.promo-text{font-size:30px;font-weight:800;line-height:1.05;color:var(--ink)}
.promo-text em{font-style:normal;color:var(--green)}
.btn{background:var(--green);color:var(--white);font-size:8px;font-weight:700;padding:7px 14px;display:inline-block}

/* section titles */
.section-title{text-align:center;font-size:15px;font-weight:700;margin:34px 0 16px;letter-spacing:.5px}
.view--mobile .section-title{font-size:10px;margin:20px 0 10px}

/* products */
.products{display:grid;gap:16px 20px;margin:0 40px}
.products--four{grid-template-columns:repeat(4,1fr)}
.products--two{grid-template-columns:repeat(2,1fr);margin:0 20px;gap:10px 14px}
.product{text-align:center;font-size:7px;line-height:1.5}
.shoe{height:84px;margin-bottom:6px;background:radial-gradient(ellipse at center,#6f86a5 0 30%,#f2f2f2 55%)}
.shoe.s-white{background:radial-gradient(ellipse at center,#cfcfcf 0 30%,#f6f6f6 55%)}
.shoe.s-pink{background:radial-gradient(ellipse at center,#e6a9b7 0 30%,#f6f6f6 55%)}
.shoe.s-black{background:radial-gradient(ellipse at center,#262626 0 30%,#f4f4f4 55%)}
.shoe.s-green{background:radial-gradient(ellipse at center,#2d3b2a 0 28%,#86c46b 38%,#f4f4f4 58%)}
.view--mobile .shoe{height:56px}
.product-brand{color:var(--blue);font-weight:700}
.product-name{color:var(--muted)}
.price-old{color:var(--muted);text-decoration:line-through;margin-right:4px}
.price{color:var(--red);font-weight:700}
.pager{text-align:center;font-size:8px;color:var(--muted);margin-top:18px}
.pager b{display:inline-block;border:1px solid var(--line);padding:3px 8px;font-weight:600}

/* news */
.news{display:grid;grid-template-columns:repeat(3,1fr);gap:14px;margin:0 24px}
.news-photo{height:128px}
.news-head{color:var(--green);font-size:7px;font-weight:700;margin:6px 0 3px}
.news-text{font-size:7px;color:var(--muted);line-height:1.5}

/* photo strip */
.strip{display:grid;grid-template-columns:repeat(4,1fr);gap:5px;margin:24px 24px 0}
.strip .tile{height:180px}

/* brands */
.brands{display:flex;justify-content:space-around;align-items:center;margin:0 30px;font-size:11px;font-weight:700;color:var(--ink)}
.view--mobile .brands{flex-wrap:wrap;gap:8px 14px;justify-content:center;font-size:8px;margin:0 16px}

/* perks */
.perks{display:grid;grid-template-columns:repeat(4,1fr);gap:14px;margin:24px 24px 0}
.perk{border:1px solid var(--line);height:60px;display:flex;align-items:center;gap:10px;padding:0 12px;font-size:8px;font-weight:700;line-height:1.3}
.perk svg{width:22px;height:22px;flex:none}
.view--mobile .perks{grid-template-columns:1fr;margin:18px 30px 0;gap:10px}
.view--mobile .perk{flex-direction:column;justify-content:center;height:96px;text-align:center;gap:8px;background:#f6f6f6;border:none}

/* footer */
.footer{background:var(--footer);color:var(--footer-text);margin-top:auto;padding:26px 24px 12px;font-size:8px;line-height:1.7}
.footer-cols{display:grid;grid-template-columns:1.4fr 1fr 1fr 1fr;gap:20px}
.footer h4{color:var(--white);font-size:10px;margin-bottom:8px}
.field{background:var(--white);height:18px;margin-bottom:6px;color:var(--muted);padding:0 6px;display:flex;align-items:center}
.social{display:flex;gap:5px;margin-bottom:10px}
.social i{width:12px;height:12px;background:var(--footer-text);border-radius:50%;display:block}
.badge{width:42px;height:16px;border-radius:8px;background:var(--footer-text)}
.copyright{text-align:center;border-top:1px solid #3a3a3a;margin-top:18px;padding-top:8px;font-size:7px}
.view--mobile .footer-cols{grid-template-columns:1fr;gap:18px}
.view--mobile .footer{padding:20px 16px 10px}

/* mobile specifics */
.view--mobile .topbar{padding:0 12px;height:40px}
.view--mobile .logo{font-size:17px}
.view--mobile .navbar{padding:0 12px}
.view--mobile .search{width:200px}
.view--mobile .hero{margin:8px 10px 0;height:130px}
.view--mobile .hero-panel{width:50%;padding:12px 10px}
.view--mobile .hero-title{font-size:11px;margin-bottom:8px}
.view--mobile .select{height:14px;margin-bottom:5px;font-size:6px}
.view--mobile .tile{height:78px}
.promo--mobile{margin:8px 10px 0;height:40px;padding:0 12px;font-size:14px}
.news-card--mobile{margin:0 20px}
.news-card--mobile .news-photo{height:110px}
.stack{display:flex;flex-direction:column;gap:6px;margin:18px 10px 0}
.stack .tile{height:104px}
</style>
</head>
<body>

<!-- Desktop view -->
<main class="view view--desktop">
  <header>
    <div class="topbar">
      <div class="logo"><span class="logo-mark"></span>KELVARO</div>
      <div class="header-icons">
        <svg viewBox="0 0 16 16"><circle cx="8" cy="5" r="3" fill="none" stroke="#2b2b2b" stroke-width="1.5"/><path d="M2 15c1-4 11-4 12 0" fill="none" stroke="#2b2b2b" stroke-width="1.5"/></svg>
        <svg viewBox="0 0 16 16"><path d="M8 14 2 8a3.5 3.5 0 0 1 6-4 3.5 3.5 0 0 1 6 4z" fill="none" stroke="#2b2b2b" stroke-width="1.5"/></svg>
        <svg viewBox="0 0 16 16"><path d="M1 2h3l2 9h8l2-6H5" fill="none" stroke="#2b2b2b" stroke-width="1.5"/><circle cx="7" cy="14" r="1.2" fill="#2b2b2b"/><circle cx="13" cy="14" r="1.2" fill="#2b2b2b"/></svg>
      </div>
    </div>
    <nav class="navbar">
      <div class="search">Search…<svg width="8" height="8" viewBox="0 0 10 10"><circle cx="4" cy="4" r="3" fill="none" stroke="#8a8a8a"/><path d="M6.5 6.5 9 9" stroke="#8a8a8a"/></svg></div>
      <div class="nav-links"><span>DAM</span><span>HERR</span><span>BARN</span></div>
    </nav>
  </header>

  <section class="hero">
    <div class="hero-panel">
      <div class="hero-title">SEARCH FOR FAVORITE SHOES HERE!</div>
      <div class="select">Select Brand <span>▾</span></div>
      <div class="select">Select Style <span>▾</span></div>
      <div class="select">Select Size <span>▾</span></div>
    </div>
    <div class="hero-photo" role="img" aria-label="Photo of many pairs of shoes on a wooden floor"></div>
  </section>

  <section class="tiles tiles--four">
    <div class="tile"><div class="tile-photo tone-a" role="img" aria-label="Boots photo"></div><div class="tile-label">BOOTS</div></div>
    <div class="tile"><div class="tile-photo tone-b" role="img" aria-label="Sneakers photo"></div><div class="tile-label">SNEAKERS</div></div>
    <div class="tile"><div class="tile-photo tone-c" role="img" aria-label="Sandals photo"></div><div class="tile-label">SANDALS</div></div>
    <div class="tile"><div class="tile-photo tone-d" role="img" aria-label="Loafers photo"></div><div class="tile-label">LOAFERS</div></div>
    <div class="tile"><div class="tile-photo tone-e" role="img" aria-label="Ankle boots photo"></div><div class="tile-label">ANKLE BOOTS</div></div>
    <div class="tile"><div class="tile-photo tone-b" role="img" aria-label="Heels photo"></div><div class="tile-label">HEELS</div></div>
    <div class="tile"><div class="tile-photo tone-f" role="img" aria-label="Running shoes photo"></div><div class="tile-label">RUNNING</div></div>
    <div class="tile"><div class="tile-photo tone-a" role="img" aria-label="Ballerinas photo"></div><div class="tile-label">BALLERINAS</div></div>
    <div class="tile"><div class="tile-photo tone-d" role="img" aria-label="Slippers photo"></div><div class="tile-label">SLIPPERS</div></div>
    <div class="tile"><div class="tile-photo tone-c" role="img" aria-label="Pumps photo"></div><div class="tile-label">PUMPS</div></div>
    <div class="tile"><div class="tile-photo tone-f" role="img" aria-label="Canvas shoes photo"></div><div class="tile-label">CANVAS</div></div>
    <div class="tile"><div class="tile-photo tone-e" role="img" aria-label="Winter boots photo"></div><div class="tile-label">WINTER</div></div>
    <div class="tile"><div class="tile-photo tone-c" role="img" aria-label="Rubber boots photo"></div><div class="tile-label">RUBBER BOOTS</div></div>
    <div class="tile"><div class="tile-photo tone-a" role="img" aria-label="Clogs photo"></div><div class="tile-label">CLOGS</div></div>
    <div class="tile"><div class="tile-photo tone-b" role="img" aria-label="Kids shoes photo"></div><div class="tile-label">KIDS</div></div>
    <div class="tile"><div class="tile-photo tone-d" role="img" aria-label="Accessories photo"></div><div class="tile-label">ACCESSORIES</div></div>
  </section>

  <section class="promo" role="img" aria-label="Banner with men's leather shoes">
    <div class="promo-text"><em>20% OFF</em><br>ON MEN'S SHOES</div>
    <span class="btn">SHOP NOW</span>
  </section>

  <section>
    <h2 class="section-title">FEATURED PRODUCTS</h2>
    <div class="products products--four">
      <div class="product"><div class="shoe" role="img" aria-label="Blue sneaker"></div><div class="product-brand">NORVIK</div><div class="product-name">Runner Low Blue</div><span class="price-old">899kr</span><span class="price">699kr</span></div>
      <div class="product"><div class="shoe s-white" role="img" aria-label="White sneaker"></div><div class="product-brand">ALDRA</div><div class="product-name">Court Classic White</div><span class="price-old">999kr</span><span class="price">749kr</span></div>
      <div class="product"><div class="shoe s-pink" role="img" aria-label="Pink sneaker"></div><div class="product-brand">VELSTO</div><div class="product-name">Slip Pastel Pink</div><span class="price-old">699kr</span><span class="price">499kr</span></div>
      <div class="product"><div class="shoe s-black" role="img" aria-label="Black sneaker"></div><div class="product-brand">RIVONA</div><div class="product-name">Street Black</div><span class="price-old">949kr</span><span class="price">699kr</span></div>
      <div class="product"><div class="shoe s-white" role="img" aria-label="Grey sneaker"></div><div class="product-brand">NORVIK</div><div class="product-name">Air Light Grey</div><span class="price-old">1099kr</span><span class="price">799kr</span></div>
      <div class="product"><div class="shoe s-green" role="img" aria-label="Black and green sneaker"></div><div class="product-brand">ALDRA</div><div class="product-name">Trail Green</div><span class="price-old">1199kr</span><span class="price">899kr</span></div>
      <div class="product"><div class="shoe s-black" role="img" aria-label="Black running shoe"></div><div class="product-brand">SOLDEN</div><div class="product-name">Run Pro Black</div><span class="price-old">999kr</span><span class="price">749kr</span></div>
      <div class="product"><div class="shoe s-black" role="img" aria-label="Black leather sneaker"></div><div class="product-brand">ESKEL</div><div class="product-name">City Leather</div><span class="price-old">1299kr</span><span class="price">999kr</span></div>
    </div>
    <div class="pager"><b>Page 1 of 10 ›</b></div>
  </section>

  <section>
    <h2 class="section-title">NEWS</h2>
    <div class="news">
      <article><div class="news-photo tone-e" role="img" aria-label="Photo of leather boots"></div><div class="news-head">AUTUMN BOOTS HAVE ARRIVED</div><p class="news-text">Warm lining and sturdy soles for wet days. Find your new pair in our fresh collection today.</p></article>
      <article><div class="news-photo tone-a" role="img" aria-label="Photo of tying shoelaces"></div><div class="news-head">HOW TO CARE FOR LEATHER</div><p class="news-text">Simple steps to keep your shoes clean and soft. Our guide covers polish, brushes and storage.</p></article>
      <article><div class="news-photo tone-d" role="img" aria-label="Photo of shoes on a shelf"></div><div class="news-head">TRENDS OF THE SEASON</div><p class="news-text">Chunky soles, earthy tones and classic loafers lead the way this year in every wardrobe.</p></article>
    </div>
  </section>

  <section>
    <h2 class="section-title">FAVORITES</h2>
    <div class="products products--four">
      <div class="product"><div class="shoe s-green" role="img" aria-label="Sport sandal"></div><div class="product-brand">SOLDEN</div><div class="product-name">Sandal Trek</div><span class="price-old">599kr</span><span class="price">449kr</span></div>
      <div class="product"><div class="shoe s-black" role="img" aria-label="Black sandal"></div><div class="product-brand">DRAVEL</div><div class="product-name">Strap Black</div><span class="price-old">799kr</span><span class="price">599kr</span></div>
      <div class="product"><div class="shoe s-black" role="img" aria-label="Black loafer"></div><div class="product-brand">ESKEL</div><div class="product-name">Loafer Classic</div><span class="price-old">1099kr</span><span class="price">849kr</span></div>
      <div class="product"><div class="shoe s-black" role="img" aria-label="Black pump"></div><div class="product-brand">TUNDREK</div><div class="product-name">Pump Noir</div><span class="price-old">899kr</span><span class="price">649kr</span></div>
    </div>
  </section>

  <section class="strip">
    <div class="tile"><div class="tile-photo tone-e" role="img" aria-label="Photo of brown boots"></div><div class="tile-label">BOOTS</div></div>
    <div class="tile"><div class="tile-photo tone-a" role="img" aria-label="Photo of shoes on steps"></div><div class="tile-label">SHOES</div></div>
    <div class="tile"><div class="tile-photo tone-c" role="img" aria-label="Photo of sneakers outdoors"></div><div class="tile-label">SNEAKERS</div></div>
    <div class="tile"><div class="tile-photo tone-f" role="img" aria-label="Photo of sandals"></div><div class="tile-label">SANDALS</div></div>
  </section>

  <section>
    <h2 class="section-title">TOP BRANDS</h2>
    <div class="brands"><span>Norvik</span><span>Solden</span><span>Aldra</span><span>Dravel</span><span>Tundrek</span><span>Rivona</span><span>Velsto</span><span>Eskel</span></div>
  </section>

  <section class="perks">
    <div class="perk"><svg viewBox="0 0 24 24"><path d="M3 20l6-2 12-12-4-4L5 14z" fill="#5cb85c"/></svg>Always all Shoes in stock!</div>
    <div class="perk"><svg viewBox="0 0 24 24"><path d="M4 12l5 5L20 6" fill="none" stroke="#5cb85c" stroke-width="3"/></svg>Always 30 days open purchase!</div>
    <div class="perk"><svg viewBox="0 0 24 24"><rect x="1" y="7" width="13" height="10" fill="#5cb85c"/><path d="M14 10h5l3 3v4h-8z" fill="#5cb85c"/><circle cx="6" cy="18" r="2" fill="#fff" stroke="#5cb85c"/><circle cx="18" cy="18" r="2" fill="#fff" stroke="#5cb85c"/></svg>Always Free Shipping and Free Return!</div>
    <div class="perk"><svg viewBox="0 0 24 24"><path d="M12 2l8 4v6c0 5-4 9-8 10-4-1-8-5-8-10V6z" fill="#5cb85c"/></svg>Always price guarantee!</div>
  </section>

  <footer class="footer" style="margin-top:24px">
    <div class="footer-cols">
      <div><h4>Newsletter</h4><div class="field">Your email address</div><span class="btn">Sign Up</span></div>
      <div><h4>Site Map</h4>Women<br>Men<br>Kids<br>Brands</div>
      <div><h4>Contact Info</h4>Lindvägen 14, Kelby<br>+46 8 555 01 23<br>info@kelvaro.se</div>
      <div><h4>Follow Us</h4><div class="social"><i></i><i></i><i></i><i></i><i></i></div><div class="badge"></div></div>
    </div>
    <div class="copyright">Copyright © 2024 Kelvaro. All rights reserved.</div>
  </footer>
</main>

<!-- Mobile view -->
<main class="view view--mobile">
  <header>
    <div class="topbar">
      <div class="logo"><span class="logo-mark"></span>KELVARO</div>
      <div class="header-icons">
        <svg viewBox="0 0 16 16"><path d="M8 14 2 8a3.5 3.5 0 0 1 6-4 3.5 3.5 0 0 1 6 4z" fill="none" stroke="#2b2b2b" stroke-width="1.5"/></svg>
        <svg viewBox="0 0 16 16"><path d="M1 2h3l2 9h8l2-6H5" fill="none" stroke="#2b2b2b" stroke-width="1.5"/></svg>
      </div>
    </div>
    <nav class="navbar">
      <svg width="12" height="10" viewBox="0 0 12 10"><path d="M0 1h12M0 5h12M0 9h12" stroke="#2b2b2b" stroke-width="1.5"/></svg>
      <div class="search">Search…</div>
    </nav>
  </header>

  <section class="hero">
    <div class="hero-panel">
      <div class="hero-title">SEARCH FOR FAVORITE SHOES HERE!</div>
      <div class="select">Brand <span>▾</span></div>
      <div class="select">Style <span>▾</span></div>
      <div class="select">Size <span>▾</span></div>
    </div>
    <div class="hero-photo" role="img" aria-label="Photo of many pairs of shoes"></div>
  </section>

  <section class="tiles tiles--two">
    <div class="tile"><div class="tile-photo tone-a" role="img" aria-label="Boots photo"></div><div class="tile-label">BOOTS</div></div>
    <div class="tile"><div class="tile-photo tone-b" role="img" aria-label="Sneakers photo"></div><div class="tile-label">SNEAKERS</div></div>
    <div class="tile"><div class="tile-photo tone-c" role="img" aria-label="Sandals photo"></div><div class="tile-label">SANDALS</div></div>
    <div class="tile"><div class="tile-photo tone-d" role="img" aria-label="Loafers photo"></div><div class="tile-label">LOAFERS</div></div>
    <div class="tile"><div class="tile-photo tone-e" role="img" aria-label="Ankle boots photo"></div><div class="tile-label">ANKLE BOOTS</div></div>
    <div class="tile"><div class="tile-photo tone-f" role="img" aria-label="Running shoes photo"></div><div class="tile-label">RUNNING</div></div>
    <div class="tile"><div class="tile-photo tone-a" role="img" aria-label="Heels photo"></div><div class="tile-label">HEELS</div></div>
    <div class="tile"><div class="tile-photo tone-d" role="img" aria-label="Kids shoes photo"></div><div class="tile-label">KIDS</div></div>
  </section>

  <section class="promo promo--mobile" role="img" aria-label="Banner with men's shoes">
    <div class="promo-text" style="font-size:14px"><em>20% OFF</em></div>
  </section>

  <section>
    <h2 class="section-title">FEATURED PRODUCTS</h2>
    <div class="products products--two">
      <div class="product"><div class="shoe" role="img" aria-label="Blue sneaker"></div><div class="product-brand">NORVIK</div><span class="price-old">899kr</span><span class="price">699kr</span></div>
      <div class="product"><div class="shoe s-black" role="img" aria-label="Black sneaker"></div><div class="product-brand">RIVONA</div><span class="price-old">949kr</span><span class="price">699kr</span></div>
    </div>
  </section>

  <section>
    <h2 class="section-title">NEWS</h2>
    <article class="news-card--mobile"><div class="news-photo tone-e" role="img" aria-label="Photo of leather boots"></div><div class="news-head">AUTUMN BOOTS HAVE ARRIVED</div><p class="news-text">Warm lining and sturdy soles for wet days ahead.</p></article>
  </section>

  <section>
    <h2 class="section-title">FAVORITES</h2>
    <div class="products products--two">
      <div class="product"><div class="shoe s-green" role="img" aria-label="Sport sandal"></div><div class="product-brand">SOLDEN</div><span class="price-old">599kr</span><span class="price">449kr</span></div>
      <div class="product"><div class="shoe s-black" role="img" aria-label="Black loafer"></div><div class="product-brand">ESKEL</div><span class="price-old">1099kr</span><span class="price">849kr</span></div>
    </div>
  </section>

  <section class="stack">
    <div class="tile"><div class="tile-photo tone-e" role="img" aria-label="Photo of brown boots"></div><div class="tile-label">BOOTS</div></div>
    <div class="tile"><div class="tile-photo tone-a" role="img" aria-label="Photo of shoes on steps"></div><div class="tile-label">SHOES</div></div>
    <div class="tile"><div class="tile-photo tone-c" role="img" aria-label="Photo of sneakers"></div><div class="tile-label">SNEAKERS</div></div>
    <div class="tile"><div class="tile-photo tone-f" role="img" aria-label="Photo of sandals"></div><div class="tile-label">SANDALS</div></div>
  </section>

  <section>
    <h2 class="section-title">TOP BRANDS</h2>
    <div class="brands"><span>Norvik</span><span>Solden</span><span>Aldra</span><span>Dravel</span><span>Tundrek</span><span>Eskel</span></div>
  </section>

  <section class="perks">
    <div class="perk"><svg viewBox="0 0 24 24"><path d="M3 20l6-2 12-12-4-4L5 14z" fill="#5cb85c"/></svg>Always all Shoes in stock!</div>
    <div class="perk"><svg viewBox="0 0 24 24"><rect x="1" y="7" width="13" height="10" fill="#5cb85c"/><path d="M14 10h5l3 3v4h-8z" fill="#5cb85c"/></svg>Always Free Shipping and Free Return!</div>
    <div class="perk"><svg viewBox="0 0 24 24"><path d="M4 12l5 5L20 6" fill="none" stroke="#5cb85c" stroke-width="3"/></svg>Always 30 days open purchase!</div>
    <div class="perk"><svg viewBox="0 0 24 24"><path d="M12 2l8 4v6c0 5-4 9-8 10-4-1-8-5-8-10V6z" fill="#5cb85c"/></svg>Always price guarantee!</div>
  </section>

  <footer class="footer">
    <div class="footer-cols">
      <div><h4>Newsletter</h4><div class="field">Your email address</div><span class="btn">Sign Up</span></div>
      <div><h4>Site Map</h4>Women<br>Men<br>Kids<br>Brands</div>
      <div><h4>Contact Info</h4>Lindvägen 14, Kelby<br>+46 8 555 01 23<br>info@kelvaro.se</div>
      <div><h4>Follow Us</h4><div class="social"><i></i><i></i><i></i><i></i><i></i></div><div class="badge"></div></div>
    </div>
    <div class="copyright">Copyright © 2024 Kelvaro</div>
  </footer>
</main>

</body>
</html>
```